Personal Development Business needs a Business Card Design Project

We need a buiness card design for a new Personal Development business based in S. NSW in Australia called "Willow Path Within. Our target market is to women who are looking to re-enter the workforce, or already be in the workforce at the middle management level. As a result of consultations their outcomes will be, but not exclusive to: increased confidence, increased self esteem and self awareness, work-life balance, time management, positive thinking.
Behind the scenes of coaching and mentoring will be a spiritual "bent".
Anticipate a beautiful candle as a possible background - showing success and shining - see attachment which came off Framevault. Colours - Unsure until I see something that "grabs my attention". Not esoteric fluffy design but something that suggests safe, professional, supportive of personal journey without being too corporate.
Look forward to what you come up with.
Some designers have been requesting various bits of information.
Personal information. See attachment.
Two-sided please.
Gold lines at all four edges.
Many thanks
Mira
Business

```html
<!DOCTYPE html>
<html lang="en">
<head>
<meta charset="utf-8">
<title>Willow Path Within – Business Card</title>
<link rel="stylesheet" href="https://fonts.googleapis.com/css2?family=Noto+Sans:wght@400;700&display=swap">
<style>
  :root {
    --card-bg: #fdfbfd;
    --ink-purple: #6b2c8f;
    --frame-gold: #d9b227;
    --dot-gold: #f0b01c;
    --band-gold: #c98a2e;
    --band-violet: #8a3fb0;
    --band-lilac: #c9b6e4;
    --photo-green: #4f8a2c;
    --photo-teal: #2fb3a6;
    --photo-blue: #3e8fe0;
    --photo-violet: #6a2a9a;
    --photo-deep: #2a0f3e;
  }
  html, body {
    margin: 0;
    padding: 0;
    width: 1200px;
    height: 686px;
    overflow: hidden;
    background: var(--card-bg);
  }
  .card {
    position: relative;
    width: 1200px;
    height: 686px;
    background: var(--card-bg);
    font-family: "Noto Sans", Arial, sans-serif;
    color: var(--ink-purple);
    overflow: hidden;
  }
  .gold-frame {
    position: absolute;
    left: 21px;
    top: 25px;
    width: 1164px;
    height: 634px;
    border: 2px solid var(--frame-gold);
  }
  .candle-panel {
    position: absolute;
    left: 0;
    top: 0;
    width: 480px;
    height: 686px;
  }
  .line {
    position: absolute;
    right: 63px;
    margin: 0;
    line-height: 1;
    white-space: nowrap;
    text-align: right;
  }
  .name { top: 78px; font-size: 55px; font-weight: 400; }
  .credential { font-size: 34px; }
  .cred-1 { top: 138px; }
  .cred-2 { top: 185px; }
  .cred-3 { top: 228px; }
  .contact { font-size: 35px; }
  .website { top: 357px; font-weight: 700; }
  .mobile { top: 400px; }
  .email { top: 445px; }
  .contact strong { font-weight: 700; margin-left: 10px; }
  .focus-areas {
    position: absolute;
    right: 63px;
    top: 596px;
    margin: 0;
    padding: 0;
    list-style: none;
    display: flex;
    align-items: center;
    font-size: 30px;
    line-height: 1;
    white-space: nowrap;
  }
  .focus-areas li { display: flex; align-items: center; }
  .focus-areas li + li::before {
    content: "";
    width: 10px;
    height: 10px;
    border-radius: 50%;
    background: var(--dot-gold);
    margin: 0 26px;
  }
</style>
</head>
<body>
<div class="card">
  <div class="gold-frame"></div>

  <svg class="candle-panel" viewBox="0 0 480 686" role="img" aria-label="Photograph of a glowing candle in green, blue and violet tones">
    <defs>
      <linearGradient id="photoTones" x1="0" y1="0" x2="0.3" y2="1">
        <stop offset="0" stop-color="var(--photo-green)"/>
        <stop offset="0.3" stop-color="var(--photo-teal)"/>
        <stop offset="0.55" stop-color="var(--photo-blue)"/>
        <stop offset="0.8" stop-color="var(--photo-violet)"/>
        <stop offset="1" stop-color="var(--photo-deep)"/>
      </linearGradient>
      <radialGradient id="flameGlow" cx="0.16" cy="0.36" r="0.35">
        <stop offset="0" stop-color="#ffffff" stop-opacity="0.9"/>
        <stop offset="0.35" stop-color="#d8f3ff" stop-opacity="0.45"/>
        <stop offset="1" stop-color="#ffffff" stop-opacity="0"/>
      </radialGradient>
    </defs>
    <path d="M0 0 H346 C430 70 440 200 340 320 C250 420 210 520 270 610 C290 640 305 665 312 686 H0 Z" fill="var(--band-gold)"/>
    <path d="M0 0 H326 C410 70 420 200 320 316 C230 416 190 520 250 610 C270 640 285 665 292 686 H0 Z" fill="var(--band-violet)"/>
    <path d="M0 0 H306 C390 70 400 200 300 312 C210 412 170 520 230 610 C250 640 265 665 272 686 H0 Z" fill="var(--band-lilac)"/>
    <path d="M0 0 H288 C372 70 382 200 282 308 C192 408 152 520 212 610 C232 640 247 665 254 686 H0 Z" fill="url(#photoTones)"/>
    <path d="M0 0 H288 C372 70 382 200 282 308 C192 408 152 520 212 610 C232 640 247 665 254 686 H0 Z" fill="url(#flameGlow)"/>
  </svg>

  <h1 class="line name">Mira Ellwood</h1>
  <p class="line credential cred-1">Grad Dip (Mgt) RVU</p>
  <p class="line credential cred-2">BA American History (HCU)</p>
  <p class="line credential cred-3">Master NLP</p>

  <p class="line contact website">willowpathwithin.com.au</p>
  <p class="line contact mobile">Mobile:<strong>0412 586 903</strong></p>
  <p class="line contact email">Email:<strong>miraatwillow@bellbird.com.au</strong></p>

  <ul class="focus-areas">
    <li>Self Awareness</li>
    <li>Confidence</li>
    <li>Work-Life Balance</li>
  </ul>
</div>
</body>
</html>
```